Torvel Letterhead

Hi Kaleno:

I would like a card that is cleanly laid out, with adequate white space for the text to breathe. We don't need a fax number.
The address is:
4170 Brindle Parkway, Suite 812
Plano Texas 75311

Marcus T. Elwood
Managing Director
469.531.7746 (d)
214.690.3858 (m)
melwood@torvelholdings.example

The Kanji characters for Torvel are: 光路
It would be good if you could fit the kanji in as well.

Thank you, Marcus

```html
<!DOCTYPE html>
<html lang="en">
<head>
<meta charset="utf-8">
<title>Torvel Business Card</title>
<link rel="stylesheet" href="https://fonts.googleapis.com/css2?family=Arimo:ital,wght@0,400;0,700;1,400&display=swap">
<style>
  :root {
    --backdrop: #3a3438;
    --card: #f4ecc9;
    --card-edge: #e8dcaf;
    --brand: #6a5726;
    --ink: #4b4a3c;
    --name: #574a20;
    --muted: #8a8770;
    --rule: #bdb596;
  }
  * { box-sizing: border-box; margin: 0; padding: 0; }
  html, body {
    width: 1200px; height: 800px; overflow: hidden;
    background: var(--backdrop);
  }
  .canvas {
    width: 1200px; height: 800px;
    display: flex; align-items: center; justify-content: center;
  }
  .card {
    position: relative;
    width: 1050px; height: 600px;
    background: radial-gradient(ellipse at 35% 30%, #f7f0d3 0%, var(--card) 55%, var(--card-edge) 100%);
    box-shadow: 0 18px 40px rgba(0,0,0,0.35);
  }
  .brand {
    position: absolute; left: 100px; top: 150px;
    display: flex; align-items: center; gap: 18px;
    font-family: "Arimo", sans-serif; font-weight: 400;
    font-size: 64px; line-height: 1; letter-spacing: 2px;
    color: var(--brand);
  }
  .brand__square {
    width: 22px; height: 22px; flex: none;
    background: var(--brand);
  }
  .identity {
    position: absolute; left: 566px; top: 196px;
    font-family: "Arimo", sans-serif; color: var(--ink);
  }
  .identity__name { font-size: 30px; letter-spacing: 0.5px; }
  .identity__name b { font-weight: 700; color: var(--name); }
  .identity__title { font-size: 19px; font-style: italic; color: var(--muted); margin-top: 4px; }
  .contact {
    position: absolute; left: 500px; top: 318px;
    padding-left: 22px; border-left: 1.5px solid var(--rule);
    font-family: "Arimo", sans-serif; color: var(--ink);
    font-size: 20px; line-height: 1.3;
    list-style: none;
  }
  .contact__item { display: flex; align-items: flex-start; gap: 14px; margin-bottom: 6px; }
  .contact__icon { width: 18px; height: 22px; flex: none; margin-top: 2px; fill: var(--muted); }
  .contact__item--email { margin-top: 10px; }
</style>
</head>
<body>
<div class="canvas">
  <div class="card">
    <div class="brand">
      <span class="brand__square" aria-hidden="true"></span>
      <span class="brand__name">Torvel</span>
    </div>

    <div class="identity">
      <div class="identity__name"><b>MARCUS T.</b> ELWOOD</div>
      <div class="identity__title">Managing Director</div>
    </div>

    <ul class="contact">
      <li class="contact__item">
        <svg class="contact__icon" viewBox="0 0 18 22"><path d="M9 1a7 7 0 0 0-7 7c0 5 7 13 7 13s7-8 7-13a7 7 0 0 0-7-7zm0 10a3 3 0 1 1 0-6 3 3 0 0 1 0 6z"/></svg>
        <span>4170 Brindle Parkway, Suite 812<br>Plano Texas 75311</span>
      </li>
      <li class="contact__item">
        <svg class="contact__icon" viewBox="0 0 18 22"><rect x="2" y="3" width="14" height="17" rx="2"/><rect x="5" y="6" width="8" height="4" fill="var(--card)"/></svg>
        <span>469.531.7746</span>
      </li>
      <li class="contact__item">
        <svg class="contact__icon" viewBox="0 0 18 22"><rect x="4" y="1" width="10" height="20" rx="2"/><rect x="6" y="4" width="6" height="12" fill="var(--card)"/></svg>
        <span>214.690.3858</span>
      </li>
      <li class="contact__item contact__item--email">
        <svg class="contact__icon" viewBox="0 0 18 22"><rect x="1" y="5" width="16" height="12" rx="1"/><path d="M1.5 5.5 9 12l7.5-6.5" fill="none" stroke="var(--card)" stroke-width="1.5"/></svg>
        <span>melwood@torvelholdings.example</span>
      </li>
    </ul>
  </div>
</div>
</body>
</html>
```